Lakemont Hydro Partners, Inc. Company Brochure

I would like someone to design a brochure that can be handed out to prospective clients. We are a full service water and wastewater operations company that provides services to Municipal Utility Districts and citys. I would like something that is catchy to the eye and reflects a company that prides itself on providing personal service to its clients. We need to revamp our website, that's next, but the website does have a description of our company and services offered. You can find that information at www.lakemonthydropartners.example

```html
<!DOCTYPE html>
<html lang="en">
<head>
<meta charset="utf-8">
<title>Lakemont Hydro Partners, Inc. – Company Brochure</title>
<link href="https://fonts.googleapis.com/css2?family=Roboto:wght@400;500&family=Open+Sans:wght@400;600;700&display=swap" rel="stylesheet">
<style>
  :root {
    --page-bg: #e4e6e8;
    --paper: #ffffff;
    --brand-blue: #1f7fc4;
    --ink-blue: #2a73b5;
    --body-grey: #7b8794;
    --water-light: #3fb6df;
    --water-mid: #1c86c8;
    --water-deep: #0d4f9a;
    --inside-text: #ffffff;
    --bubble-light: #c9eef8;
    --bubble-dark: #2b8fbe;
  }
  * { box-sizing: border-box; margin: 0; padding: 0; }
  html, body { width: 1200px; height: 1000px; overflow: hidden; }
  body {
    background: var(--page-bg);
    font-family: "Open Sans", Arial, sans-serif;
    position: relative;
  }
  .panel {
    position: absolute;
    top: 245px;
    width: 360px;
    height: 510px;
    overflow: hidden;
    box-shadow: 0 6px 18px rgba(0,0,0,.18);
  }

  /* Front cover */
  .cover { left: 40px; background: var(--paper); font-family: "Roboto", Arial, sans-serif; }
  .cover-title {
    position: absolute; left: 18px; top: 20px; right: 60px;
    font-weight: 500; font-size: 17px; color: var(--brand-blue); line-height: 1.2;
  }
  .cover-mark {
    position: absolute; right: 18px; top: 14px; width: 32px; height: 32px;
    border-radius: 50%; border: 2px solid var(--brand-blue);
  }
  .cover-intro {
    position: absolute; left: 18px; right: 18px; top: 68px;
    font-size: 7.6px; line-height: 1.42; color: var(--body-grey);
  }
  .cover-splash {
    position: absolute; left: 0; right: 0; bottom: 0; height: 300px;
    background:
      linear-gradient(180deg, var(--paper) 0%, rgba(255,255,255,0) 28%),
      linear-gradient(165deg, #bfe0f2 20%, #5aa6d8 50%, #2f7fbd 70%, #a9cfea 100%);
  }
  .cover-contact {
    position: absolute; right: 18px; top: 212px; text-align: right;
    color: var(--ink-blue); font-size: 11px; line-height: 1.45;
  }
  .cover-tagline { font-size: 13.5px; margin-bottom: 6px; }
  .cover-address { font-size: 9.5px; }
  .cover-web { font-size: 11px; font-weight: 500; margin-top: 3px; }

  /* Inside spread */
  .inside {
    background: linear-gradient(160deg, var(--water-light) 0%, var(--water-mid) 55%, var(--water-deep) 100%);
    color: var(--inside-text);
  }
  .inside-left { left: 420px; }
  .inside-right { left: 780px; box-shadow: 6px 6px 18px rgba(0,0,0,.18); }
  .inside-right::before {
    content: ""; position: absolute; left: 0; top: 0; bottom: 0; width: 14px;
    background: linear-gradient(90deg, rgba(0,0,0,.12), rgba(0,0,0,0));
  }
  .bubble {
    position: absolute; width: 74px; height: 74px; border-radius: 50%;
    background: radial-gradient(circle at 35% 30%, var(--bubble-light) 0%, #7fcbe6 45%, var(--bubble-dark) 100%);
    border: 2px solid rgba(255,255,255,.6);
    display: flex; align-items: center; justify-content: center; text-align: center;
    font-weight: 700; font-size: 12px; line-height: 1.1; color: #fff;
    text-shadow: 0 1px 2px rgba(0,0,0,.35);
  }
  .about-bubble { left: 16px; top: 16px; }
  .about-text {
    position: absolute; left: 16px; right: 16px; top: 16px;
    font-size: 10.6px; line-height: 1.5;
  }
  .about-text::before { content: ""; float: left; width: 82px; height: 78px; }
  .photo-strip {
    position: absolute; left: 0; right: 0; bottom: 0; height: 104px;
    display: flex; gap: 4px; padding: 0 0 0 0;
  }
  .photo { flex: 1; }
  .photo-drink { background: linear-gradient(135deg, #6d8a4b, #c8b08a 55%, #9bc3a0); }
  .photo-pool { background: linear-gradient(135deg, #9fd3ea, #3f9cd0 60%, #d8c2a8); }
  .photo-splash { background: linear-gradient(135deg, #4aa8d8, #c9e7f4 50%, #2f7fbd); }

  .services-bubble { left: 14px; top: 16px; }
  .services-intro {
    position: absolute; left: 100px; right: 14px; top: 14px;
    font-size: 9.6px; line-height: 1.45; font-weight: 600;
  }
  .service-list {
    position: absolute; top: 124px; list-style: none;
    font-size: 8.6px; line-height: 1.3; width: 158px;
  }
  .service-list.col-a { left: 18px; }
  .service-list.col-b { left: 186px; }
  .service-list li { position: relative; padding-left: 13px; margin-bottom: 5px; }
  .service-list li::before {
    content: ""; position: absolute; left: 0; top: 2px; width: 7px; height: 7px;
    border: 1.2px solid #fff; border-radius: 50%;
  }
  .mission-bubble { left: 14px; top: 292px; width: 80px; height: 80px; }
  .mission-text {
    position: absolute; left: 16px; right: 14px; top: 290px;
    font-size: 10.2px; line-height: 1.5; font-weight: 700;
  }
  .mission-text::before { content: ""; float: left; width: 88px; height: 84px; }
</style>
</head>
<body>

<section class="panel cover" aria-label="Front cover">
  <h1 class="cover-title">Lakemont Hydro Partners Inc.</h1>
  <div class="cover-mark" aria-hidden="true"></div>
  <p class="cover-intro">Lakemont Hydro Partners, Inc. is a leading competitor in the utility operations industry and has achieved this status by maintaining the quality of work and relationships that few companies can offer. Whether you are a District that is currently operated by an outside contract company or a District entertaining the concept, Lakemont Hydro Partners, Inc. would be delighted to present a detailed quote for operations and services. Please contact our office and a representative will discuss the services that are currently available in your area.</p>
  <div class="cover-splash" role="img" aria-label="Photograph of clear water splashing in a wave with rising bubbles"></div>
  <div class="cover-contact">
    <p class="cover-tagline">We are a 24/7 Operations Company!</p>
    <p>Call 555-014-0103</p>
    <p>Fax 555-014-0104</p>
    <p>Toll Free 800-555-0199</p>
    <p class="cover-address">2480 Lakeshore Road, Suite 210</p>
    <p class="cover-address">Marlow, Texas 77001</p>
    <p class="cover-web">www.lakemonthydropartners.example</p>
  </div>
</section>

<section class="panel inside inside-left" aria-label="About us">
  <div class="bubble about-bubble">About<br>Us</div>
  <p class="about-text">Lakemont Hydro Partners, Inc. was incorporated in the state of Texas in 1983. Lakemont Hydro Partners, Inc. is a water and waste water utility operations and billing company. All personnel employed by Lakemont Hydro Partners, Inc. are licensed by the TCEQ in water &amp; waste water operations and obtain the proper training needed to successfully operate treatment plants to their maximum capability. We are certified to operate surface water, ground water, and waste water treatment facilities to their maximum capability. We have a fully staffed billing and collections office to handle any of your customers needs. The mission of Lakemont Hydro Partners, Inc. is to provide the consumer with the highest caliber of services available. Our goal is to achieve this service for the Districts with the most competitive cost around.</p>
  <div class="photo-strip">
    <div class="photo photo-drink" role="img" aria-label="Photograph of a child drinking from a water fountain"></div>
    <div class="photo photo-pool" role="img" aria-label="Photograph of children swimming in a pool"></div>
    <div class="photo photo-splash" role="img" aria-label="Photograph of a child playing in splashing water"></div>
  </div>
</section>

<section class="panel inside inside-right" aria-label="Services and mission">
  <div class="bubble services-bubble">Services<br>Offered</div>
  <p class="services-intro">Lakemont Hydro Partners, Inc. is a “full service” operations company that handles all aspects of operations in the water/waste water utility industry. Here at Lakemont Hydro Partners, Inc. we feel that it is important to provide the highest caliber of services available to the Districts in which we operate. We offer the ability to tailor our services based on the current needs of the District.</p>
  <ul class="service-list col-a">
    <li>Surface Water Plant Operations</li>
    <li>Waste Water Plant Operations</li>
    <li>Ground Water Well Operations</li>
    <li>Distribution and Collection System maintenance and repairs</li>
    <li>New Construction Water and Sewer Taps and all inspections required</li>
    <li>Billing and Collections</li>
    <li>Park and Trail maintenance</li>
  </ul>
  <ul class="service-list col-b">
    <li>Meter Reading</li>
    <li>Consulting/Management</li>
    <li>Lab Work and Reporting to any and all regulating agencies</li>
    <li>Project Planning</li>
    <li>Assist in Annual Budget Planning</li>
    <li>Smoke Testing</li>
    <li>Detention pond maintenance</li>
  </ul>
  <div class="bubble mission-bubble">Our<br>Mission<br>&amp;<br>Vision</div>
  <p class="mission-text">Lakemont Hydro Partners, Inc.’s mission is to produce and deliver potable drinking water and treat residential wastewater in a safe, reliable, efficient, and environmentally sound manner. Our vision is to be the recognized performance leader of the waste and wastewater utility industry. Being a performance leader means we will achieve operational excellence, industry-leading customer satisfaction and superior financial performance.</p>
</section>

</body>
</html>
```